Vantor Glide - Stock Certificate

We need a custom designed stock certificate that represents the look of our company logo but also have a cool look compared to a standard stock certificate. We thinking we want the logo in gold. Our website is https://www.vantorglideusa.example.

We are wanting the certificate to look very professional and really cool, we have sales agents that work for the company and we are creating a program by which the sales agents can gain ownership in the company. So the certificates need to have a very cool appeal and that provides a sense of pride in owning "Units" in Vantor Glide.
Updates

Reason: Extending so other board members can vote as well, thank you all!

Target Market(s)

Stock/Shareholders

Industry/Entity Type

It Company

Font styles to use
Script

Requirements
Must have
• Must look like a stock certificate, must use our logo which the psd file for it was attached.
Nice to have
• Nice to have the logo in gold

```html
<!DOCTYPE html>
<html lang="en">
<head>
<meta charset="utf-8">
<title>Vantor Glide – Stock Certificate</title>
<link href="https://fonts.googleapis.com/css2?family=Fondamento:ital@0;1&display=swap" rel="stylesheet">
<style>
  :root {
    --frame: #222222;
    --panel: #a0a0a0;
    --ink: #111111;
    --badge-ring: #3a3a3a;
    --badge-core: #232323;
    --badge-text: #d9a63a;
  }
  html, body {
    margin: 0;
    padding: 0;
    width: 1200px;
    height: 927px;
    overflow: hidden;
    background: var(--frame);
  }
  .certificate {
    display: block;
    width: 1200px;
    height: 927px;
  }
  .frame { fill: var(--frame); }
  .panel { fill: var(--panel); }
  .badge-ring { fill: var(--badge-ring); }
  .badge-core { fill: var(--badge-core); }
  .badge-name {
    font-family: "Fondamento", cursive;
    font-size: 30px;
    fill: var(--badge-text);
  }
  .title {
    font-family: "Fondamento", cursive;
    font-style: italic;
    font-size: 92px;
    fill: var(--ink);
  }
  .phrase {
    font-family: "Fondamento", cursive;
    font-style: italic;
    font-size: 36px;
    fill: var(--ink);
  }
  .fill-line {
    stroke: var(--ink);
    stroke-width: 3;
  }
</style>
</head>
<body>
<svg class="certificate" viewBox="0 0 1200 927" xmlns="http://www.w3.org/2000/svg" role="document" aria-label="Vantor Glide stock certificate">
  <rect class="frame" x="0" y="0" width="1200" height="927"/>
  <rect class="panel" x="38" y="38" width="1124" height="851"/>

  <g class="badge">
    <circle class="badge-ring" cx="230" cy="199" r="125"/>
    <circle class="badge-core" cx="230" cy="199" r="105"/>
    <text class="badge-name" x="230" y="210" text-anchor="middle">Vantor Glide</text>
  </g>

  <text class="title" x="436" y="222">stock certificate</text>
  <text class="phrase" x="702" y="306" text-anchor="middle">This is to certify that</text>
  <line class="fill-line" x1="280" y1="382" x2="1140" y2="382"/>

  <text class="phrase" x="125" y="484">Is the owner of</text>
  <line class="fill-line" x1="378" y1="484" x2="667" y2="484"/>
  <text class="phrase" x="683" y="484">shares of stock of</text>
  <line class="fill-line" x1="943" y1="484" x2="1126" y2="484"/>

  <line class="fill-line" x1="133" y1="567" x2="582" y2="567"/>
  <text class="phrase" x="598" y="567">on the</text>
  <line class="fill-line" x1="701" y1="567" x2="992" y2="567"/>
  <text class="phrase" x="1006" y="567">day of</text>

  <line class="fill-line" x1="125" y1="660" x2="417" y2="660"/>
  <text class="phrase" x="422" y="660">In the year</text>
  <line class="fill-line" x1="612" y1="660" x2="742" y2="660"/>
  <text class="phrase" x="742" y="660">At</text>
  <line class="fill-line" x1="793" y1="660" x2="1110" y2="660"/>
  <text class="phrase" x="1113" y="660">.</text>

  <text class="phrase" x="675" y="753">Signed,</text>
  <line class="fill-line" x1="814" y1="753" x2="1131" y2="753"/>
  <text class="phrase" x="681" y="832">Signed,</text>
  <line class="fill-line" x1="816" y1="832" x2="1136" y2="832"/>
</svg>
</body>
</html>
```